Design a 4 page brochure

Design a 4 page (A4 size) brochure for our company . It means 8 sides of A4 sheets.
You can use any pictures from internet to make it beautiful but if there are any people in the picture it should be Indian like faces. Our company is new so we cant provide any pictures to you.

For content you can use the old tri foldbrochure which we had but dont use the same old design and also ............ another broucher of Korunesh foundation is a sample broucher to take contents only not any other things

the name of the company is VELORIMAN FOUNDATION
it has its website as [login to view URL]
it has 2 departments or divisions
1. Opening windows..... which focuses on value education in schools
[login to view URL] hearts ..shadow dance or light dance based on values of life. take content from the silver lanterns facebook page...[login to view URL] - you can give one sheet only for this.......

```html
<!DOCTYPE html>
<html lang="en">
<head>
<meta charset="utf-8">
<title>Veloriman Foundation – Brochure</title>
<link href="https://fonts.googleapis.com/css2?family=Oswald:wght@400;500;600&family=Roboto:ital,wght@0,300;0,400;1,300&display=swap" rel="stylesheet">
<style>
:root{
  --backdrop:#646464;
  --paper:#f1e9e1;
  --peach:#f8c98e;
  --orange:#f2873a;
  --magenta:#e4007c;
  --pink-soft:#f16fa9;
  --heading:#d9145c;
  --ink:#5f5656;
  --ink-soft:#8a7f7f;
  --sun:#f9c623;
}
*{box-sizing:border-box;margin:0;padding:0}
html,body{width:1200px;height:3235px;overflow:hidden}
body{background:var(--backdrop);position:relative;font-family:'Roboto',sans-serif;color:var(--ink)}

.page{position:absolute;width:520px;height:735px;background:var(--paper);overflow:hidden}
.spread{position:absolute;left:80px;width:1040px;height:735px;box-shadow:0 10px 30px rgba(0,0,0,.35)}
.spread .page{top:0}
.spread .page.left{left:0}
.spread .page.right{left:520px}
.spine{position:absolute;left:500px;top:0;width:40px;height:735px;
  background:linear-gradient(90deg,rgba(0,0,0,0) 0,rgba(0,0,0,.10) 50%,rgba(0,0,0,0) 100%);z-index:5}

.cover-single{left:340px;top:59px;box-shadow:0 10px 30px rgba(0,0,0,.35)}
.row-2{top:853px}
.row-3{top:1647px}
.row-4{top:2441px}

/* cover */
.art{position:absolute;left:0;top:0;width:520px;height:735px}
.cover-photo{position:absolute;left:-20px;top:178px;width:430px;height:410px;border-radius:50%;
  background:radial-gradient(circle at 45% 40%,#c99a7c 0,#8a5a44 45%,#3e2a24 100%)}
.cover-thumb{position:absolute;left:182px;top:552px;width:96px;height:96px;border-radius:50%;
  border:4px solid var(--paper);background:radial-gradient(circle,#b48a70,#5b4034)}
.brand{position:absolute;display:flex;align-items:center;gap:6px;
  font-family:'Oswald',sans-serif;font-weight:500;font-size:10px;letter-spacing:.08em;color:var(--heading)}
.brand .dot{width:24px;height:24px;border-radius:50%;border:2px solid var(--heading)}
.cover .brand{left:250px;top:26px}
.cover-title{position:absolute;left:220px;top:70px;width:250px}
.cover-title .kicker{font-family:'Oswald',sans-serif;font-weight:400;font-size:21px;letter-spacing:.12em;color:var(--ink-soft)}
.cover-title h1{font-family:'Oswald',sans-serif;font-weight:600;font-size:25px;color:var(--heading);line-height:1.1;letter-spacing:.02em;white-space:nowrap}
.cover-title p{font-style:italic;font-weight:300;font-size:10px;line-height:1.35;margin-top:4px;color:var(--ink)}

/* inner pages */
.petals-top{position:absolute;left:0;top:0;width:520px;height:120px}
.left .petals-top{background:
  linear-gradient(to bottom,rgba(241,233,225,0) 40%,var(--paper) 100%),
  linear-gradient(90deg,#f9c623 0,#f8b23c 45%,#f3a8b6 85%,#ee8fb0 100%)}
.right .petals-top{background:
  linear-gradient(to bottom,rgba(241,233,225,0) 40%,var(--paper) 100%),
  linear-gradient(90deg,#ee8fb0 0,#f3a8b6 35%,#f8b23c 75%,#f9c623 100%)}
.petals-bottom{position:absolute;bottom:0;height:90px;
  background:radial-gradient(ellipse at 50% 100%,#f9c623 0,#fbd65c 45%,rgba(249,198,35,0) 72%)}
.left .petals-bottom{left:140px;width:260px}
.right .petals-bottom{left:-40px;width:240px}

h2{font-family:'Oswald',sans-serif;font-weight:500;font-size:13px;color:var(--heading);letter-spacing:.02em;text-transform:uppercase}
.body-text{font-size:9px;line-height:1.45;font-weight:300;color:var(--ink)}
.body-text p+p{margin-top:8px}

.intro{position:absolute;left:40px;top:140px;width:180px}
.intro h2{margin-bottom:4px}
.intro-photo{position:absolute;left:250px;top:150px;width:180px;height:116px;
  background:linear-gradient(135deg,#7c8fb0 0,#b7c4d8 55%,#8aa06a 100%);border:3px solid #fff}
.bullets{position:absolute;left:40px;width:440px;list-style:none}
.bullets li{position:relative;padding-left:22px;font-size:9px;line-height:1.45;font-weight:300}
.bullets li+li{margin-top:12px}
.bullets li::before{content:"";position:absolute;left:2px;top:2px;border-left:7px solid var(--heading);border-top:4px solid transparent;border-bottom:4px solid transparent}
.bullets.one{top:320px}
.missing{position:absolute;left:40px;top:380px;width:440px;text-align:center;font-size:17px}
.bullets.two{top:430px}

.litmus{position:absolute;left:40px;top:132px;width:440px}
.litmus h2{margin-bottom:6px}
.aspects{position:absolute;left:40px;top:240px;width:440px;display:grid;grid-template-columns:1fr 1fr;column-gap:30px;row-gap:24px}
.aspect header{display:flex;align-items:center;gap:8px;margin-bottom:6px}
.aspect header svg{width:24px;height:24px;flex:none}
.aspect h3{font-family:'Oswald',sans-serif;font-weight:500;font-size:10px;color:var(--heading);text-transform:uppercase}

/* back cover */
.about{position:absolute;left:270px;top:120px;width:220px}
.about h2{margin-bottom:6px}
.back .brand{left:50px;top:262px}
.contacts{position:absolute;left:210px;top:290px;list-style:none;font-size:9px;font-weight:300}
.contacts li{display:flex;align-items:center;gap:8px;margin-bottom:9px}
.contacts svg{width:14px;height:14px;flex:none}
.back-photo{position:absolute;left:20px;top:455px;width:190px;height:190px;border-radius:50%;
  border:5px solid var(--paper);background:radial-gradient(circle at 50% 45%,#c99a7c 0,#7b5140 55%,#3c2a24 100%)}
</style>
</head>
<body>

<!-- Front cover -->
<section class="page cover cover-single">
  <svg class="art" viewBox="0 0 520 735" aria-hidden="true">
    <rect width="520" height="735" fill="var(--paper)"/>
    <path d="M0 470 C150 600 350 560 520 420 V735 H0Z" fill="var(--peach)"/>
    <path d="M420 175 C490 215 515 320 500 460 L520 460 V250 C500 215 470 190 420 175Z" fill="var(--pink-soft)"/>
  </svg>
  <div class="cover-photo" role="img" aria-label="Photo of a smiling young student"></div>
  <svg class="art" viewBox="0 0 520 735" aria-hidden="true">
    <path d="M0 490 C140 565 330 565 520 440 V470 C330 600 140 600 0 520Z" fill="var(--pink-soft)"/>
    <path d="M0 520 C140 600 330 600 520 470 V530 C330 660 140 660 0 590Z" fill="var(--magenta)"/>
    <path d="M0 590 C140 660 330 660 520 530 V580 C330 700 140 700 0 640Z" fill="var(--orange)"/>
  </svg>
  <div class="cover-thumb" role="img" aria-label="Small photo of two young schoolchildren"></div>
  <div class="brand"><span class="dot"></span>VELORIMAN FOUNDATION</div>
  <div class="cover-title">
    <div class="kicker">TEACHHING VALUES</div>
    <h1>THROUGH EVERY DAY LIFE</h1>
    <p>Encourage values as empowering tools in meeting the challenges of contemporary social world.</p>
  </div>
</section>

<!-- Inner spread (flat) -->
<section class="spread row-2">
  <div class="page left">
    <div class="petals-top" role="img" aria-label="Decorative flower petal pattern"></div>
    <div class="intro">
      <h2>Introduction</h2>
      <div class="body-text">
        <p>Veloriman Foundation, a voluntary organisation, is dedicated to assist school students inculcate moral values, by organizing seminars, courses and inter-school contests.</p>
        <p>The values professed are based on the eternal principles underlying common teachings of all great scriptures across the globe.</p>
      </div>
    </div>
    <div class="intro-photo" role="img" aria-label="Photo of two children seated beside the words Teaching Values through Everyday Life"></div>
    <ul class="bullets one">
      <li>These serious issues faced by the educated and economically flourishing future citizens convince the leaders and intelligent class of society that “SOMETHING IS SERIOUSLY MISSING” in the Modern Education system.</li>
    </ul>
    <h2 class="missing">“Something is seriously missing”</h2>
    <ul class="bullets two">
      <li>The missing link is the comprehensive approach needed for the overall development of students. The art of balancing character and competence is necessary for the students to be better equipped to face the challenges of the dynamic world today.</li>
      <li>The course emphasizes on the need of embracing values that can guide the students to become successful individuals without compromising on character, at various stages in their personal and professional lives.</li>
    </ul>
    <div class="petals-bottom" role="img" aria-label="Decorative flower petal pattern"></div>
  </div>
  <div class="page right">
    <div class="petals-top" role="img" aria-label="Decorative flower petal pattern"></div>
    <div class="litmus">
      <h2>The Quadruple Litmus Test</h2>
      <div class="body-text">
        <p>There are four principle aspects to the character of a person with strong value system in his life, through which one can evaluate the percentage of values imbibed and moral duties discharged.</p>
        <p>This Quadruple Litmus Test of character, although qualitative, can be seen as a yardstick to judge the holistic growth of the person. The Quadruple aspects cover the following:</p>
      </div>
    </div>
    <div class="aspects">
      <article class="aspect">
        <header><svg viewBox="0 0 24 24"><rect x="3" y="14" width="18" height="8" fill="var(--heading)"/><circle cx="12" cy="5" r="3" fill="var(--heading)"/><rect x="9" y="8" width="6" height="6" fill="var(--heading)"/></svg><h3>Personal Growth</h3></header>
        <p class="body-text">Success is a multi-faceted word, different for every individual. However, the definition of success cannot be confined to just monetary prosperity. Growing with integrity and morality to a sustained position in life is real success.</p>
      </article>
      <article class="aspect">
        <header><svg viewBox="0 0 24 24"><circle cx="12" cy="12" r="9" fill="none" stroke="var(--heading)" stroke-width="2"/><path d="M3 12H21M12 3C8 8 8 16 12 21M12 3C16 8 16 16 12 21" fill="none" stroke="var(--heading)" stroke-width="1.5"/></svg><h3>Social Responsibility</h3></header>
        <p class="body-text">The society fulfils countless needs and demands of a person since its birth. Moreover, the unlimited resources that Mother Nature has given us, needs to be utilized and preserved, judiciously.</p>
      </article>
      <article class="aspect">
        <header><svg viewBox="0 0 24 24"><circle cx="5" cy="9" r="3" fill="var(--heading)"/><circle cx="12" cy="7" r="3" fill="var(--heading)"/><circle cx="19" cy="9" r="3" fill="var(--heading)"/><rect x="2" y="13" width="20" height="7" rx="3" fill="var(--heading)"/></svg><h3>Interpersonal Relationships</h3></header>
        <p class="body-text">A man cannot sustain alone, without healthy relationships. Strong sense of respect, understanding and compassion for superiors, peers and subordinates respectively makes a person more capable of handling provoking situations.</p>
      </article>
      <article class="aspect">
        <header><svg viewBox="0 0 24 24"><path d="M2 6C6 4 10 5 12 7C14 5 18 4 22 6V19C18 17 14 18 12 20C10 18 6 17 2 19Z" fill="var(--heading)"/></svg><h3>Spiritual Awakening</h3></header>
        <p class="body-text">Throughout the history, most compassionate and loving people have been those who have lived a God-centered life and served others as parts and parcels of God.</p>
      </article>
    </div>
    <div class="petals-bottom" role="img" aria-label="Decorative flower petal pattern"></div>
  </div>
  <div class="spine"></div>
</section>

<!-- Inner spread, second view -->
<section class="spread row-3">
  <div class="page left">
    <div class="petals-top" role="img" aria-label="Decorative flower petal pattern"></div>
    <div class="intro">
      <h2>Introduction</h2>
      <div class="body-text">
        <p>Veloriman Foundation, a voluntary organisation, is dedicated to assist school students inculcate moral values, by organizing seminars, courses and inter-school contests.</p>
        <p>The values professed are based on the eternal principles underlying common teachings of all great scriptures across the globe.</p>
      </div>
    </div>
    <div class="intro-photo" role="img" aria-label="Photo of two children seated beside the words Teaching Values through Everyday Life"></div>
    <ul class="bullets one">
      <li>These serious issues faced by the educated and economically flourishing future citizens convince the leaders and intelligent class of society that “SOMETHING IS SERIOUSLY MISSING” in the Modern Education system.</li>
    </ul>
    <h2 class="missing">“Something is seriously missing”</h2>
    <ul class="bullets two">
      <li>The missing link is the comprehensive approach needed for the overall development of students. The art of balancing character and competence is necessary for the students to be better equipped to face the challenges of the dynamic world today.</li>
      <li>The course emphasizes on the need of embracing values that can guide the students to become successful individuals without compromising on character, at various stages in their personal and professional lives.</li>
    </ul>
    <div class="petals-bottom" role="img" aria-label="Decorative flower petal pattern"></div>
  </div>
  <div class="page right">
    <div class="petals-top" role="img" aria-label="Decorative flower petal pattern"></div>
    <div class="litmus">
      <h2>The Quadruple Litmus Test</h2>
      <div class="body-text">
        <p>There are four principle aspects to the character of a person with strong value system in his life, through which one can evaluate the percentage of values imbibed and moral duties discharged.</p>
        <p>This Quadruple Litmus Test of character, although qualitative, can be seen as a yardstick to judge the holistic growth of the person. The Quadruple aspects cover the following:</p>
      </div>
    </div>
    <div class="aspects">
      <article class="aspect">
        <header><svg viewBox="0 0 24 24"><rect x="3" y="14" width="18" height="8" fill="var(--heading)"/><circle cx="12" cy="5" r="3" fill="var(--heading)"/><rect x="9" y="8" width="6" height="6" fill="var(--heading)"/></svg><h3>Personal Growth</h3></header>
        <p class="body-text">Success is a multi-faceted word, different for every individual. However, the definition of success cannot be confined to just monetary prosperity. Growing with integrity and morality to a sustained position in life is real success.</p>
      </article>
      <article class="aspect">
        <header><svg viewBox="0 0 24 24"><circle cx="12" cy="12" r="9" fill="none" stroke="var(--heading)" stroke-width="2"/><path d="M3 12H21M12 3C8 8 8 16 12 21M12 3C16 8 16 16 12 21" fill="none" stroke="var(--heading)" stroke-width="1.5"/></svg><h3>Social Responsibility</h3></header>
        <p class="body-text">The society fulfils countless needs and demands of a person since its birth. Moreover, the unlimited resources that Mother Nature has given us, needs to be utilized and preserved, judiciously.</p>
      </article>
      <article class="aspect">
        <header><svg viewBox="0 0 24 24"><circle cx="5" cy="9" r="3" fill="var(--heading)"/><circle cx="12" cy="7" r="3" fill="var(--heading)"/><circle cx="19" cy="9" r="3" fill="var(--heading)"/><rect x="2" y="13" width="20" height="7" rx="3" fill="var(--heading)"/></svg><h3>Interpersonal Relationships</h3></header>
        <p class="body-text">A man cannot sustain alone, without healthy relationships. Strong sense of respect, understanding and compassion for superiors, peers and subordinates respectively makes a person more capable of handling provoking situations.</p>
      </article>
      <article class="aspect">
        <header><svg viewBox="0 0 24 24"><path d="M2 6C6 4 10 5 12 7C14 5 18 4 22 6V19C18 17 14 18 12 20C10 18 6 17 2 19Z" fill="var(--heading)"/></svg><h3>Spiritual Awakening</h3></header>
        <p class="body-text">Throughout the history, most compassionate and loving people have been those who have lived a God-centered life and served others as parts and parcels of God.</p>
      </article>
    </div>
    <div class="petals-bottom" role="img" aria-label="Decorative flower petal pattern"></div>
  </div>
  <div class="spine"></div>
</section>

<!-- Back and front cover spread -->
<section class="spread row-4">
  <div class="page left back">
    <svg class="art" viewBox="0 0 520 735" aria-hidden="true">
      <rect width="520" height="735" fill="var(--paper)"/>
      <path d="M0 0 H520 V70 C380 115 150 115 0 80Z" fill="var(--peach)"/>
      <path d="M0 0 H520 V30 C380 70 150 70 0 40Z" fill="var(--orange)"/>
      <path d="M0 600 C180 680 360 700 520 660 V735 H0Z" fill="var(--peach)"/>
      <path d="M0 560 C180 640 360 680 520 625 V650 C360 705 180 665 0 590Z" fill="var(--pink-soft)"/>
      <path d="M0 590 C180 665 360 705 520 650 V690 C360 740 180 700 0 630Z" fill="var(--magenta)"/>
      <path d="M0 630 C180 700 360 740 520 690 V715 C360 760 180 725 0 660Z" fill="var(--orange)"/>
    </svg>
    <div class="about">
      <h2>About Us -</h2>
      <p class="body-text">Currently we are conducting value education programs in schools across the city and nearby towns. We also conduct training seminars and workshops for teachers and parents, helping them nurture character, compassion and leadership in young minds, rooted in timeless principles.</p>
    </div>
    <div class="brand"><span class="dot"></span>VELORIMAN FOUNDATION</div>
    <ul class="contacts">
      <li><svg viewBox="0 0 24 24"><path d="M6 3L9 3L11 8L8.5 9.5C9.5 12 12 14.5 14.5 15.5L16 13L21 15V18C21 19.5 19.5 21 18 21C10 20 4 14 3 6C3 4.5 4.5 3 6 3Z" fill="var(--heading)"/></svg>+91 90000 24680</li>
      <li><svg viewBox="0 0 24 24"><rect x="2" y="5" width="20" height="14" rx="2" fill="var(--heading)"/><path d="M3 6L12 13L21 6" fill="none" stroke="var(--paper)" stroke-width="1.6"/></svg>hello@veloriman.org</li>
      <li><svg viewBox="0 0 24 24"><path d="M12 2C8 2 5 5 5 9C5 14 12 22 12 22C12 22 19 14 19 9C19 5 16 2 12 2Z" fill="var(--heading)"/><circle cx="12" cy="9" r="2.5" fill="var(--paper)"/></svg>12 Lotus Lane, Civil Lines, Nagpur</li>
    </ul>
    <div class="back-photo" role="img" aria-label="Photo of two smiling students"></div>
  </div>
  <div class="page right cover">
    <svg class="art" viewBox="0 0 520 735" aria-hidden="true">
      <rect width="520" height="735" fill="var(--paper)"/>
      <path d="M0 470 C150 600 350 560 520 420 V735 H0Z" fill="var(--peach)"/>
      <path d="M420 175 C490 215 515 320 500 460 L520 460 V250 C500 215 470 190 420 175Z" fill="var(--pink-soft)"/>
    </svg>
    <div class="cover-photo" role="img" aria-label="Photo of a smiling young student"></div>
    <svg class="art" viewBox="0 0 520 735" aria-hidden="true">
      <path d="M0 490 C140 565 330 565 520 440 V470 C330 600 140 600 0 520Z" fill="var(--pink-soft)"/>
      <path d="M0 520 C140 600 330 600 520 470 V530 C330 660 140 660 0 590Z" fill="var(--magenta)"/>
      <path d="M0 590 C140 660 330 660 520 530 V580 C330 700 140 700 0 640Z" fill="var(--orange)"/>
    </svg>
    <div class="cover-thumb" role="img" aria-label="Small photo of two young schoolchildren"></div>
    <div class="brand"><span class="dot"></span>VELORIMAN FOUNDATION</div>
    <div class="cover-title">
      <div class="kicker">TEACHHING VALUES</div>
      <h1>THROUGH EVERY DAY LIFE</h1>
      <p>Encourage values as empowering tools in meeting the challenges of contemporary social world.</p>
    </div>
  </div>
  <div class="spine"></div>
</section>

</body>
</html>
```